Roofing Company needs Business card design

We need a business card design for our roofing contracting company. We do Residential and commercial roofing. Design need to be modern, professional and clean. The design should communicate quality and professionalism. We would like to have rounded corners, but open to your ideas.
Company Name: Kestrel roofing Solutions
Company Address: (dummy text)
Name on business card: (dummy text)
And following lines:
Storm damage specialists
commercial & residential
shingles, flat and metal roofs./
Open to background colors.
I have ai. and eps files of logo if needed.
just let me know.
Mostly residential customers but we do commercial too.
Roofing

```html
<!DOCTYPE html>
<html lang="en">
<head>
<meta charset="utf-8">
<title>Kestrel Roofing Solutions – Business Card</title>
<link rel="stylesheet" href="https://fonts.googleapis.com/css2?family=Saira:wght@400;500;700;800&display=swap">
<style>
  :root {
    --backdrop: #e9e6e1;
    --card-white: #ffffff;
    --card-black: #050505;
    --ember: #e0452a;
    --ember-light: #f26a2e;
    --ink: #1c1c1c;
    --ink-soft: #555555;
    --paper-soft: #d9d9d9;
    --icon-grey: #8a98aa;
  }
  * { box-sizing: border-box; margin: 0; padding: 0; }
  html, body { width: 1200px; height: 800px; overflow: hidden; }
  body {
    background: var(--backdrop);
    font-family: "Saira", Arial, sans-serif;
    display: flex;
    align-items: center;
    justify-content: center;
    gap: 90px;
  }
  .card {
    width: 340px;
    height: 595px;
    border-radius: 34px;
    position: relative;
    overflow: hidden;
    box-shadow: 0 12px 30px rgba(0,0,0,0.18);
  }

  /* Back side */
  .card--back {
    background: var(--card-black);
    display: flex;
    flex-direction: column;
    align-items: center;
    justify-content: center;
    padding: 40px 30px;
  }
  .back-mark {
    display: flex;
    flex-direction: column;
    align-items: center;
    gap: 18px;
  }
  .back-mark__dot {
    width: 110px;
    height: 110px;
    border-radius: 50%;
    background: var(--ember);
  }
  .back-mark__name {
    color: var(--ember);
    font-weight: 800;
    font-size: 42px;
    line-height: 1;
    letter-spacing: 2px;
    text-transform: uppercase;
  }
  .services {
    margin-top: 46px;
    text-align: center;
    list-style: none;
  }
  .services__item {
    color: var(--paper-soft);
    font-size: 15px;
    line-height: 1.7;
    letter-spacing: 1.5px;
    text-transform: uppercase;
  }
  .services__item--lead {
    color: var(--ember-light);
    font-weight: 700;
  }

  /* Front side */
  .card--front {
    background: var(--card-white);
    padding: 58px 30px 40px;
    display: flex;
    flex-direction: column;
    align-items: center;
  }
  .brand {
    display: flex;
    flex-direction: column;
    align-items: center;
    margin-bottom: 44px;
  }
  .brand__name {
    color: var(--ink);
    font-weight: 800;
    font-size: 50px;
    line-height: 1;
    letter-spacing: 1px;
    text-transform: uppercase;
  }
  .brand__tagline {
    color: var(--ink);
    font-weight: 500;
    font-size: 14px;
    letter-spacing: 5px;
    text-transform: uppercase;
    margin-top: 6px;
  }
  .person { text-align: center; }
  .person__name {
    color: var(--ember);
    font-weight: 800;
    font-size: 22px;
    line-height: 1.1;
    letter-spacing: 1.5px;
    text-transform: uppercase;
  }
  .person__role {
    color: var(--ink);
    font-size: 13px;
    margin-top: 2px;
  }
  .rule {
    height: 2px;
    background: var(--ember-light);
    margin: 12px 0 14px;
  }
  .rule--wide { width: 190px; }
  .rule--short { width: 90px; margin-top: 18px; }
  .contact {
    text-align: center;
    color: var(--ink);
    font-size: 17px;
    line-height: 1.4;
    letter-spacing: 0.5px;
  }
  .contact__address { margin-bottom: 16px; }
  .social {
    display: flex;
    gap: 8px;
    margin-top: 22px;
    align-self: flex-start;
    margin-left: 70px;
  }
  .social__icon {
    width: 24px;
    height: 24px;
    border-radius: 4px;
    background: var(--icon-grey);
  }
</style>
</head>
<body>
  <div class="card card--back">
    <div class="back-mark">
      <span class="back-mark__dot"></span>
      <span class="back-mark__name">Kestrel</span>
    </div>
    <ul class="services">
      <li class="services__item services__item--lead">Storm damage specialists</li>
      <li class="services__item">Commercial &amp; residential</li>
      <li class="services__item">Shingles, flat and metal roofs</li>
    </ul>
  </div>

  <div class="card card--front">
    <div class="brand">
      <span class="brand__name">Kestrel</span>
      <span class="brand__tagline">Roofing Solutions</span>
    </div>

    <div class="person">
      <p class="person__name">Dylan Marsh</p>
      <p class="person__role">President</p>
    </div>
    <div class="rule rule--wide"></div>

    <div class="contact">
      <p class="contact__address">48 B Hollow Creek Road<br>Franklin TN 3720</p>
      <p>T: 555.318.2207</p>
      <p>F: 555.604.1183</p>
      <p>info@yoursite.com</p>
      <p>www.yoursite.com</p>
    </div>
    <div class="rule rule--short"></div>

    <div class="social" aria-label="Social media links">
      <span class="social__icon"></span>
      <span class="social__icon"></span>
      <span class="social__icon"></span>
    </div>
  </div>
</body>
</html>
```